BPL its me again- No TIME

I am a weight loss consultant who my target audience now is staff- teachers at work.

I am Bright Path Living and I have partner up with the program Vital Kickoff. I am selling my services but it will be attached to his brochure which I attached to show you.

This flyer will be given to teachers while at work or left on the staff room lunch table.

Please make it short, snappy and fun.
Why lose weight at work? People are time poor

points:-
- Mobile weight loss consultant who comes to you at work
before/after school or lunch break.
-20 minute private 1 on 1 consultations
-limited spots (3 per hour)
-no contract
-10 years experience

If possible I would like it at work flyer for different companies as well like banks but teachers/schools are my main target.

Like the picture with the teacher in front of the board but can remove the heart if possible
Thank you

i will brochure soon to show you

Target Market(s)

people at work- during lunch breaks or before and after
First is school teachers then other companies.
Females are the majority of clients

Industry/Entity Type

Teacher

Requirements
Must have
• leave it up to you just want to grab staff's attention.
Should not have
• please never use the word "diet" its a healthy lifestyle.

```html
<!DOCTYPE html>
<html lang="en">
<head>
<meta charset="UTF-8">
<title>Why Lose Weight at Work – Bright Path Living</title>
<link rel="stylesheet" href="https://fonts.googleapis.com/css2?family=Cabin+Sketch:wght@700&family=Schoolbell&display=swap">
<style>
  :root {
    --page-bg: #e9e9e9;
    --board: #2f3334;
    --chalk: #f4f4f2;
    --paper: #ffffff;
    --paper-line: #c9dcef;
    --margin-line: #e59a9a;
    --ink: #2b5aa6;
    --hole: #151515;
    --gauge-tone: #8f9496;
    --pencil-tone: #c9474a;
    --tray: #c9733d;
    --photo-top: #5e3a30;
    --photo-mid: #d6b6a4;
    --photo-low: #a3a5a8;
  }
  * { box-sizing: border-box; margin: 0; padding: 0; }
  html, body { width: 1000px; height: 1200px; overflow: hidden; background: var(--page-bg); }

  .flyer {
    position: absolute; left: 70px; top: 10px; width: 860px; height: 1180px;
    background: var(--board); border: 8px solid var(--paper); overflow: hidden;
  }

  .headline {
    position: absolute; left: 82px; top: 150px;
    font-family: "Cabin Sketch", "Comic Sans MS", cursive; font-weight: 700;
    color: var(--chalk); text-transform: uppercase; line-height: 1.05;
  }
  .headline .line-1 { display: block; font-size: 54px; }
  .headline .line-2 { display: block; font-size: 78px; }
  .headline .line-3 { display: block; font-size: 60px; margin-top: 4px; }

  .gauge-art {
    position: absolute; left: 395px; top: 85px; width: 160px; height: 100px;
    background: radial-gradient(ellipse at 50% 100%, rgba(143,148,150,.55) 0%, rgba(143,148,150,.15) 70%, transparent 100%);
  }

  .teacher-photo {
    position: absolute; left: 470px; top: 380px; width: 390px; height: 780px;
    background: linear-gradient(180deg, var(--photo-top) 0%, var(--photo-mid) 32%, var(--photo-low) 62%, var(--photo-mid) 100%);
  }

  .note {
    position: absolute; left: 14px; top: 470px; width: 500px; height: 690px;
    background: var(--paper);
    background-image:
      linear-gradient(90deg, transparent 58px, var(--margin-line) 58px, var(--margin-line) 60px, transparent 60px),
      repeating-linear-gradient(180deg, transparent 0 45px, var(--paper-line) 45px 46px);
    box-shadow: 3px 4px 10px rgba(0,0,0,.4);
  }
  .note .holes { position: absolute; left: 18px; top: 70px; display: flex; flex-direction: column; gap: 210px; }
  .note .holes span { display: block; width: 20px; height: 20px; border-radius: 50%; background: var(--hole); }

  .pencil-art {
    position: absolute; left: 0; top: 448px; width: 470px; height: 44px;
    background: linear-gradient(90deg, var(--pencil-tone) 0%, var(--pencil-tone) 82%, #efcf9f 100%);
    opacity: .9;
  }

  .points {
    position: absolute; left: 68px; top: 76px; width: 420px; list-style: none;
    font-family: "Schoolbell", "Comic Sans MS", cursive; font-size: 32px; line-height: 46px; color: var(--ink);
  }
  .points li { padding-left: 18px; text-indent: -18px; }
  .points li::before { content: "•"; font-size: 20px; display: inline-block; width: 18px; text-indent: 0; }

  .brand {
    position: absolute; left: 110px; top: 560px; display: flex; align-items: center; gap: 12px;
    font-family: "Schoolbell", "Comic Sans MS", cursive; font-size: 30px; line-height: 34px; color: var(--ink);
  }
  .brand .dot { flex: none; width: 22px; height: 22px; border-radius: 50%; background: var(--ink); }

  .tray { position: absolute; left: 0; bottom: 0; width: 100%; height: 20px; background: var(--tray); }
</style>
</head>
<body>
  <main class="flyer">
    <div class="gauge-art" role="img" aria-label="Chalk speed gauge sketch"></div>

    <h1 class="headline">
      <span class="line-1">Why lose</span>
      <span class="line-2">Weight at work?</span>
      <span class="line-3">People are time poor</span>
    </h1>

    <div class="teacher-photo" role="img" aria-label="Smiling teacher in a striped top holding a green apple in front of the chalkboard"></div>

    <section class="note">
      <div class="holes"><span></span><span></span><span></span></div>
      <ul class="points">
        <li>Mobile weight loss consultant who comes to you at work before/after school or lunch break.</li>
        <li>20 minute private 1 on 1 consultations</li>
        <li>Limited spots (3 per hour)</li>
        <li>No contract</li>
        <li>10 years experience</li>
      </ul>
      <div class="brand"><span class="dot"></span>Bright Path Living</div>
    </section>

    <div class="pencil-art" role="img" aria-label="Red pencil with eraser lying across the note"></div>

    <div class="tray"></div>
  </main>
</body>
</html>
```